DJ Equipment Rental (business card/packet folder/stationary)

Designers:
The address will not longer be included in any of these designs. Thanks!

Attention designers,
It was brought to my attention that my brief was too broad and VERY confusing :/. I truly apologize.

This is what I need:
*Front and back business cards.
*A packet folder (front and back) (The size big enough to hold the 8x11 sheets)
I really don't know he size.

*Letter head

I needs to be professional, elegant, and it needs to stand out. Corporate like.

Colors:
Deep Red, Black, Deep blue . Also, follow color scheme of current logo but get creative.

Company: Vinyl Crate Hire Co
Phone: 918.555.0142
Email: Rentals@VinylCrateHireCo.example
Web: www.VinylCrateHireCo.example (under construction)
Address: 4826 W. Alder Lane, Tulsa, OK 74100
Logo: Provided

Project Deadline Extended
Reason: Due to my poor explanation and description of the project, I'm extending the due date of this project.

Target Market(s)

This folder will have my information as a business and it will serve as a marketing material. The audience range age is 18-43.

Industry/Entity Type

Business

Requirements
Must have
• Follow the color scheme provide in the logo.

```html
<!DOCTYPE html>
<html lang="en">
<head>
<meta charset="utf-8">
<title>Vinyl Crate Hire Co — Business Cards</title>
<link rel="stylesheet" href="https://fonts.googleapis.com/css2?family=Roboto:wght@400;700&display=swap">
<style>
  :root {
    --page-bg: #d8d2c8;
    --card-base: #1c1c1e;
    --card-glow: #34363a;
    --text-light: #f2f2f2;
    --text-muted: #a9abae;
    --accent-blue: #2b9fdc;
    --accent-orange: #f08a1c;
    --divider: #4a4c50;
  }
  * { box-sizing: border-box; margin: 0; padding: 0; }
  html, body {
    width: 1200px;
    height: 900px;
    overflow: hidden;
  }
  body {
    background: var(--page-bg);
    font-family: "Roboto", Arial, sans-serif;
    position: relative;
  }
  .card {
    position: absolute;
    left: 280px;
    width: 640px;
    height: 366px;
    border-radius: 4px;
    background:
      radial-gradient(ellipse 60% 55% at 50% 40%, var(--card-glow) 0%, var(--card-base) 70%);
    box-shadow: 0 10px 28px rgba(0,0,0,0.28);
    overflow: hidden;
  }
  .card--front { top: 70px; }
  .card--back  { top: 464px; }

  .brand {
    display: flex;
    align-items: center;
    gap: 12px;
    font-weight: 700;
    color: var(--text-light);
    letter-spacing: 1px;
    white-space: nowrap;
  }
  .brand__dot {
    width: 16px;
    height: 16px;
    border-radius: 50%;
    background: var(--accent-orange);
    flex: none;
  }
  .card--front .brand {
    position: absolute;
    left: 50%;
    top: 50%;
    transform: translate(-50%, -50%);
    font-size: 34px;
  }
  .card--back .brand {
    position: absolute;
    left: 150px;
    top: 96px;
    font-size: 28px;
  }

  .person {
    position: absolute;
    left: 60px;
    top: 236px;
  }
  .person__name {
    font-size: 24px;
    color: var(--text-muted);
    letter-spacing: 0.5px;
  }
  .person__first {
    font-weight: 700;
    color: var(--accent-blue);
  }
  .person__role {
    margin-top: 6px;
    margin-left: 36px;
    font-size: 17px;
    color: var(--text-muted);
  }

  .divider {
    position: absolute;
    left: 300px;
    top: 180px;
    width: 1px;
    height: 140px;
    background: var(--divider);
  }

  .contact {
    position: absolute;
    left: 324px;
    top: 186px;
    list-style: none;
  }
  .contact__item {
    display: flex;
    align-items: center;
    gap: 12px;
    height: 30px;
    font-size: 14.5px;
    color: var(--text-light);
  }
  .contact__item--phone { font-weight: 700; font-size: 16px; }
  .contact__icon {
    width: 15px;
    height: 15px;
    flex: none;
    fill: var(--accent-blue);
  }
</style>
</head>
<body>

  <section class="card card--front" aria-label="Business card front">
    <div class="brand">
      <span class="brand__dot"></span>
      <span class="brand__name">Vinyl Crate Hire Co</span>
    </div>
  </section>

  <section class="card card--back" aria-label="Business card back">
    <div class="brand">
      <span class="brand__dot"></span>
      <span class="brand__name">Vinyl Crate Hire Co</span>
    </div>

    <div class="person">
      <p class="person__name"><span class="person__first">NAME</span> SURNAME</p>
      <p class="person__role">Designation</p>
    </div>

    <div class="divider"></div>

    <ul class="contact">
      <li class="contact__item contact__item--phone">
        <svg class="contact__icon" viewBox="0 0 24 24" aria-hidden="true"><path d="M6.6 10.8a15 15 0 0 0 6.6 6.6l2.2-2.2a1 1 0 0 1 1-.25 11.4 11.4 0 0 0 3.6.57 1 1 0 0 1 1 1V20a1 1 0 0 1-1 1A17 17 0 0 1 3 4a1 1 0 0 1 1-1h3.5a1 1 0 0 1 1 1c0 1.25.2 2.45.57 3.57a1 1 0 0 1-.25 1z"/></svg>
        918.555.0142
      </li>
      <li class="contact__item">
        <svg class="contact__icon" viewBox="0 0 24 24" aria-hidden="true"><path d="M2 5h20v14H2z M4 7v1l8 5 8-5V7l-8 5z" fill-rule="evenodd"/></svg>
        Rentals@VinylCrateHireCo.example
      </li>
      <li class="contact__item">
        <svg class="contact__icon" viewBox="0 0 24 24" aria-hidden="true"><path d="M12 2a10 10 0 1 0 0 20 10 10 0 0 0 0-20zm6.9 6h-3a15 15 0 0 0-1.3-3.9A8 8 0 0 1 18.9 8zM12 4a13 13 0 0 1 1.9 4h-3.8A13 13 0 0 1 12 4zM4.3 14a8 8 0 0 1 0-4h3.4a16 16 0 0 0 0 4zm.8 2h3a15 15 0 0 0 1.3 3.9A8 8 0 0 1 5.1 16zm3-8h-3a8 8 0 0 1 4.3-3.9A15 15 0 0 0 8.1 8zM12 20a13 13 0 0 1-1.9-4h3.8A13 13 0 0 1 12 20zm2.3-6H9.7a14 14 0 0 1 0-4h4.6a14 14 0 0 1 0 4zm.3 5.9a15 15 0 0 0 1.3-3.9h3a8 8 0 0 1-4.3 3.9zm1.7-5.9a16 16 0 0 0 0-4h3.4a8 8 0 0 1 0 4z"/></svg>
        www.VinylCrateHireCo.example
      </li>
      <li class="contact__item">
        <svg class="contact__icon" viewBox="0 0 24 24" aria-hidden="true"><path d="M12 2a7 7 0 0 0-7 7c0 5.2 7 13 7 13s7-7.8 7-13a7 7 0 0 0-7-7zm0 9.5A2.5 2.5 0 1 1 12 6.5a2.5 2.5 0 0 1 0 5z"/></svg>
        4826 W. Alder Lane, Tulsa, OK 74100
      </li>
    </ul>
  </section>

</body>
</html>
```